Lumo4Kart - a fintech company - business card

We need a business card design for our Payments Technology company in Sydney, Australia. We provide business with payment solutions expanding across EFTPOS machines, online payment gateways and mobile payment solutions. We would like to see designs that are clean, classy and professional.
Target Market(s)
Business professionals, executives, c-suite
Industry/Entity Type
Fintech
Contact Information for Business Card
Will be on 400gsm. Logo will most likely be spot gloss unless designer recommends otherwise.
Font styles to use
Sans Serif
Requirements
Must have
- We need our website (lumo4kart.com.au), email (contact@lumo4kart.com.au), mobile (0432 587 904) and direct phone number (02 6815 3927) to feature on the card along with our logo (attached) and the words "EFTPOS | ONLINE | MOBILE"
- Font = Roboto

```html
<!DOCTYPE html>
<html lang="en">
<head>
<meta charset="utf-8">
<title>Lumo4Kart Business Card</title>
<link rel="stylesheet" href="https://fonts.googleapis.com/css2?family=Roboto:wght@400;500;700&display=swap">
<style>
  :root {
    --page-bg: #ececec;
    --navy-deep: #17304f;
    --navy-mid: #2a4b72;
    --frost: #d7dbde;
    --frost-light: #e4e7e9;
    --cream-text: #ece5d9;
    --brand-ink: #1c2f4b;
    --tagline-ink: #2b3036;
  }
  * { margin: 0; padding: 0; box-sizing: border-box; }
  html, body {
    width: 1200px;
    height: 969px;
    overflow: hidden;
    background: var(--page-bg);
    font-family: "Roboto", sans-serif;
  }
  .canvas {
    position: relative;
    width: 1200px;
    height: 969px;
  }
  .business-card {
    position: absolute;
    left: 100px;
    top: 200px;
    width: 1000px;
    height: 568px;
    border-radius: 22px;
    overflow: hidden;
    background: linear-gradient(100deg, var(--navy-mid) 0%, #223f63 35%, var(--navy-deep) 50%, var(--frost) 66%, var(--frost-light) 100%);
    box-shadow: 0 10px 30px rgba(0,0,0,0.18);
  }
  .decor-area {
    position: absolute;
    inset: 0;
  }
  .holder {
    position: absolute;
    left: 52px;
    top: 44px;
    color: var(--cream-text);
  }
  .holder-name {
    font-size: 34px;
    font-weight: 500;
    letter-spacing: 0.5px;
    line-height: 40px;
  }
  .holder-title {
    font-size: 23px;
    font-weight: 400;
    line-height: 28px;
    letter-spacing: 0.3px;
  }
  .divider {
    position: absolute;
    left: 55px;
    top: 130px;
    width: 333px;
    border-top: 2px dotted rgba(236,229,217,0.45);
  }
  .contact-list {
    position: absolute;
    left: 52px;
    top: 150px;
    list-style: none;
    color: var(--cream-text);
    font-size: 22px;
    line-height: 32px;
  }
  .contact-item {
    display: flex;
    align-items: center;
    height: 32px;
  }
  .contact-icon {
    width: 20px;
    height: 20px;
    margin-right: 16px;
    fill: var(--cream-text);
    flex: none;
  }
  .brand-block {
    position: absolute;
    left: 560px;
    top: 398px;
    width: 390px;
    text-align: center;
  }
  .brand-name {
    font-size: 60px;
    font-weight: 700;
    color: var(--brand-ink);
    line-height: 70px;
    letter-spacing: 0.5px;
  }
  .brand-tagline {
    font-size: 25px;
    font-weight: 400;
    color: var(--tagline-ink);
    line-height: 34px;
    letter-spacing: 0.5px;
  }
</style>
</head>
<body>
<main class="canvas">
  <section class="business-card" aria-label="Lumo4Kart business card">
    <div class="decor-area" role="img" aria-label="Decorative sweep from navy into frosted grey"></div>

    <div class="holder">
      <p class="holder-name">DANIEL HAYES</p>
      <p class="holder-title">CEO/FOUNDER</p>
    </div>
    <div class="divider"></div>

    <ul class="contact-list">
      <li class="contact-item">
        <svg class="contact-icon" viewBox="0 0 24 24" aria-hidden="true"><path d="M6.6 10.8a15.1 15.1 0 0 0 6.6 6.6l2.2-2.2a1 1 0 0 1 1-.25 11.4 11.4 0 0 0 3.6.57 1 1 0 0 1 1 1V20a1 1 0 0 1-1 1A17 17 0 0 1 3 4a1 1 0 0 1 1-1h3.5a1 1 0 0 1 1 1c0 1.25.2 2.45.57 3.57a1 1 0 0 1-.25 1z"/></svg>
        <span>02 6815 3927</span>
      </li>
      <li class="contact-item">
        <svg class="contact-icon" viewBox="0 0 24 24" aria-hidden="true"><path d="M7 1h10a2 2 0 0 1 2 2v18a2 2 0 0 1-2 2H7a2 2 0 0 1-2-2V3a2 2 0 0 1 2-2zm0 3v15h10V4z"/></svg>
        <span>0432 587 904</span>
      </li>
      <li class="contact-item">
        <svg class="contact-icon" viewBox="0 0 24 24" aria-hidden="true"><path d="M2 6h20v12H2zm2 1.5v.3l8 5 8-5v-.3zm0 2.4V16.5h16V9.9l-8 5z"/></svg>
        <span>contact@lumo4kart.com.au</span>
      </li>
      <li class="contact-item">
        <svg class="contact-icon" viewBox="0 0 24 24" aria-hidden="true"><path d="M12 2a10 10 0 1 0 0 20 10 10 0 0 0 0-20zm-1 17.9A8 8 0 0 1 4.2 10.2L9 15v1a2 2 0 0 0 2 2zm6.9-2.5A2 2 0 0 0 16 16h-1v-3a1 1 0 0 0-1-1H8v-2h2a1 1 0 0 0 1-1V7h2a2 2 0 0 0 2-2v-.4a8 8 0 0 1 2.9 12.8z"/></svg>
        <span>www.lumo4kart.com.au</span>
      </li>
    </ul>

    <div class="brand-block">
      <p class="brand-name">LUMO4KART</p>
      <p class="brand-tagline">EFTPOS | ONLINE | MOBILE</p>
    </div>
  </section>
</main>
</body>
</html>
```